Combining web page

We need a PSD webpage design for our PrestaShop store that shows food combining rules, you can see an example that we put here, you can follow the same information and food image combinations. You are just doing the design but the images when implemented on the website will be clickable that goes to product categories, all text and images will be editable.

This is just an example:
http://merrowtonic.com/content/7-food-combining-rules

Target Market(s)

Natural Product and supplement industry

Industry/Entity Type

Store

Number of Pages Required

1 page

Colors

Designer to choose colors to be used in the design.

Requirements
Must have
• 1. Clear images.
• 2. Clear readable text.
• 3. Company name shown Merrow Tonic.
• 4. Follow the food rules as seen on the web page example, but not the same design.
• 5. Logo should be seen.
• 7. All text and images will be editable.
• 8. Make sure the food images are in their proper groups.
• 9. You are not coping the design we gave you but the details have to be the same, copy the text and the image food groups are important, you cannot just put any food in a group, and the combinations are important.
Nice to have
• Here is the website it is for http://merrowtonic.com/

```html
<!DOCTYPE html>
<html lang="en">
<head>
<meta charset="utf-8">
<title>Merrow Tonic – Food Combining Chart</title>
<link rel="stylesheet" href="https://fonts.googleapis.com/css2?family=Roboto+Condensed:wght@400;700&family=Open+Sans:wght@400&display=swap">
<style>
  :root{
    --ink:#1d1d1d;
    --muted:#444;
    --band:#ececec;
    --rule:#9a9a9a;
    --c-citrus:#2a5d78;
    --c-subacid:#cc3366;
    --c-sweet:#c2bc16;
    --c-neutral:#1e6b1e;
    --c-grains:#7b1fa2;
    --c-legumes:#d23a63;
    --c-melons:#2a9fd8;
    --c-succulent:#e07a12;
    --c-veg:#5aae1a;
  }
  *{box-sizing:border-box;margin:0;padding:0}
  html,body{width:684px;height:1200px;overflow:hidden;background:#fff}
  body{position:relative;font-family:"Open Sans",sans-serif;color:var(--ink)}

  .brand{position:absolute;top:34px;left:0;width:684px;text-align:center}
  .brand-name{font-family:"Roboto Condensed",sans-serif;font-weight:400;font-size:30px;line-height:36px;color:var(--ink)}

  .chart{position:absolute;left:24px;top:119px;width:630px;border:1px solid var(--rule)}
  .chart-head,.chart-row{display:grid;grid-template-columns:270px repeat(9,40px)}
  .chart-head{height:56px}
  .chart-title{font-family:"Roboto Condensed",sans-serif;font-size:12.5px;padding:18px 0 0 27px}
  .col-head{border-left:1px solid var(--rule);text-align:center}
  .col-num{font-family:"Roboto Condensed",sans-serif;font-size:15px;height:28px;line-height:30px;border-bottom:1px solid var(--rule)}
  .col-sub{font-size:6px;line-height:8.5px;padding-top:4px;color:var(--muted)}

  .chart-row{height:94px;background:linear-gradient(var(--band),var(--band)) top/100% 84px no-repeat}
  .chart-row:last-child{height:84px}
  .group{position:relative;height:84px}
  .group-photo{position:absolute;left:2px;top:0}
  .group-text{position:absolute;left:93px;top:19px;width:172px}
  .group-name{font-family:"Roboto Condensed",sans-serif;font-size:11px;line-height:14px;margin-bottom:3px}
  .group-desc{font-size:6.6px;line-height:11.3px;color:var(--ink)}
  .cell{border-left:1px solid var(--rule);height:100%;font-family:"Roboto Condensed",sans-serif;font-size:12.5px;text-align:center;padding-top:36px}

  .principles{position:absolute;left:34px;top:1052px;width:616px;text-align:center}
  .principles h2{font-family:"Roboto Condensed",sans-serif;font-weight:400;font-size:18px;margin-bottom:14px}
  .principles p{font-size:7.3px;line-height:14.2px;color:#333}
</style>
</head>
<body>

<header class="brand">
  <div class="brand-name">Merrow Tonic</div>
</header>

<section class="chart">
  <div class="chart-head">
    <div class="chart-title">Neque porro quisquam est qui dolorem ipsum</div>
    <div class="col-head"><div class="col-num">1</div><div class="col-sub">Ipsum quia<br>dolor</div></div>
    <div class="col-head"><div class="col-num">2</div><div class="col-sub">est qui<br>dolorem</div></div>
    <div class="col-head"><div class="col-num">3</div><div class="col-sub">Ipsum quia<br>dolor</div></div>
    <div class="col-head"><div class="col-num">4</div><div class="col-sub">est qui sit<br>amet qui</div></div>
    <div class="col-head"><div class="col-num">5</div><div class="col-sub">Ipsum quia<br>dolor</div></div>
    <div class="col-head"><div class="col-num">6</div><div class="col-sub">est qui sit<br>amet qui</div></div>
    <div class="col-head"><div class="col-num">7</div><div class="col-sub">est qui<br>dolorem</div></div>
    <div class="col-head"><div class="col-num">8</div><div class="col-sub">Ipsum quia<br>dolor</div></div>
    <div class="col-head"><div class="col-num">9</div><div class="col-sub">est qui sit<br>amet qui</div></div>
  </div>

  <div class="chart-row">
    <div class="group">
      <svg class="group-photo" width="84" height="84" viewBox="0 0 84 84"><path d="M42 4A38 38 0 0 0 42 80" fill="none" stroke="var(--c-citrus)" stroke-width="5"/><defs><radialGradient id="g1"><stop offset="0" stop-color="#f6b233"/><stop offset="1" stop-color="#e46c12"/></radialGradient></defs><circle cx="45" cy="42" r="33" fill="url(#g1)" role="img" aria-label="Photo of oranges, lemons and limes"/></svg>
      <div class="group-text"><div class="group-name" style="color:var(--c-citrus)">1 CITRUS — ACID FRUITS</div><p class="group-desc">It is a long established fact that a reader will be distracted by the readable content of a page when looking at its layout. The point of using Lorem</p></div>
    </div>
    <div class="cell">XX</div><div class="cell">XX</div><div class="cell">X</div><div class="cell">XX</div><div class="cell">NR</div><div class="cell">X-NR</div><div class="cell">X</div><div class="cell">NO</div><div class="cell">NO</div>
  </div>

  <div class="chart-row">
    <div class="group">
      <svg class="group-photo" width="84" height="84" viewBox="0 0 84 84"><path d="M42 4A38 38 0 0 0 42 80" fill="none" stroke="var(--c-subacid)" stroke-width="5"/><defs><radialGradient id="g2"><stop offset="0" stop-color="#d8b33a"/><stop offset="1" stop-color="#7a3a3a"/></radialGradient></defs><circle cx="45" cy="42" r="33" fill="url(#g2)" role="img" aria-label="Photo of apples, pears, grapes and kiwi"/></svg>
      <div class="group-text"><div class="group-name" style="color:var(--c-subacid)">2 FRUITS (Sub-Acid)</div><p class="group-desc">It is a long established fact that a reader will be distracted by the readable content of a page when looking at its layout. The point of using Lorem</p></div>
    </div>
    <div class="cell">XX</div><div class="cell">XX</div><div class="cell">XX</div><div class="cell">XX</div><div class="cell">XX</div><div class="cell">X-NR</div><div class="cell">X</div><div class="cell">NO</div><div class="cell">NO</div>
  </div>

  <div class="chart-row">
    <div class="group">
      <svg class="group-photo" width="84" height="84" viewBox="0 0 84 84"><path d="M42 4A38 38 0 0 0 42 80" fill="none" stroke="var(--c-sweet)" stroke-width="5"/><defs><radialGradient id="g3"><stop offset="0" stop-color="#8a5a3c"/><stop offset="1" stop-color="#3a1d12"/></radialGradient></defs><circle cx="45" cy="42" r="33" fill="url(#g3)" role="img" aria-label="Photo of dates"/></svg>
      <div class="group-text"><div class="group-name" style="color:var(--c-sweet)">3 SWEET FRUITS — PALM FRUITS</div><p class="group-desc">It is a long established fact that a reader will be distracted by the readable content of a page when looking at its layout. The point of using Lorem</p></div>
    </div>
    <div class="cell">XX</div><div class="cell">XX</div><div class="cell">X</div><div class="cell">XX</div><div class="cell">NR</div><div class="cell">X-NR</div><div class="cell">X</div><div class="cell"></div><div class="cell">NO</div>
  </div>

  <div class="chart-row">
    <div class="group">
      <svg class="group-photo" width="84" height="84" viewBox="0 0 84 84"><path d="M42 4A38 38 0 0 0 42 80" fill="none" stroke="var(--c-neutral)" stroke-width="5"/><defs><radialGradient id="g4"><stop offset="0" stop-color="#c89a6a"/><stop offset="1" stop-color="#6a3a22"/></radialGradient></defs><circle cx="45" cy="42" r="33" fill="url(#g4)" role="img" aria-label="Photo of mixed raw nuts"/></svg>
      <div class="group-text"><div class="group-name" style="color:var(--c-neutral)">4 NEUTRAL FRUITS — RAW NUTS</div><p class="group-desc">It is a long established fact that a reader will be distracted by the readable content of a page when looking at its layout. The point of using Lorem</p></div>
    </div>
    <div class="cell">XX</div><div class="cell">XX</div><div class="cell">X</div><div class="cell">XX</div><div class="cell">NR</div><div class="cell">NO</div><div class="cell">X</div><div class="cell">NO</div><div class="cell">NO</div>
  </div>

  <div class="chart-row">
    <div class="group">
      <svg class="group-photo" width="84" height="84" viewBox="0 0 84 84"><path d="M42 4A38 38 0 0 0 42 80" fill="none" stroke="var(--c-grains)" stroke-width="5"/><defs><radialGradient id="g5"><stop offset="0" stop-color="#a0784a"/><stop offset="1" stop-color="#5a4028"/></radialGradient></defs><circle cx="45" cy="42" r="33" fill="url(#g5)" role="img" aria-label="Photo of assorted grains and seeds"/></svg>
      <div class="group-text"><div class="group-name" style="color:var(--c-grains)">5 GRAINS</div><p class="group-desc">It is a long established fact that a reader will be distracted by the readable content of a page when looking at its layout. The point of using Lorem</p></div>
    </div>
    <div class="cell">XX</div><div class="cell">XX</div><div class="cell">X</div><div class="cell">XX</div><div class="cell">NR</div><div class="cell">X-NR</div><div class="cell">X</div><div class="cell">XX</div><div class="cell">XX</div>
  </div>

  <div class="chart-row">
    <div class="group">
      <svg class="group-photo" width="84" height="84" viewBox="0 0 84 84"><path d="M42 4A38 38 0 0 0 42 80" fill="none" stroke="var(--c-legumes)" stroke-width="5"/><defs><radialGradient id="g6"><stop offset="0" stop-color="#8cc63f"/><stop offset="1" stop-color="#2f6b1a"/></radialGradient></defs><circle cx="45" cy="42" r="33" fill="url(#g6)" role="img" aria-label="Photo of brussels sprouts"/></svg>
      <div class="group-text"><div class="group-name" style="color:var(--c-legumes)">6 LEGUMES — SPROUTS</div><p class="group-desc">It is a long established fact that a reader will be distracted by the readable content of a page when looking at its layout. The point of using Lorem</p></div>
    </div>
    <div class="cell">XX</div><div class="cell">XX</div><div class="cell">XX</div><div class="cell">XX</div><div class="cell">XX</div><div class="cell">XX</div><div class="cell">X</div><div class="cell">NO</div><div class="cell">NO</div>
  </div>

  <div class="chart-row">
    <div class="group">
      <svg class="group-photo" width="84" height="84" viewBox="0 0 84 84"><path d="M42 4A38 38 0 0 0 42 80" fill="none" stroke="var(--c-melons)" stroke-width="5"/><defs><radialGradient id="g7"><stop offset="0" stop-color="#f7a94a"/><stop offset="1" stop-color="#4a4a3a"/></radialGradient></defs><circle cx="45" cy="42" r="33" fill="url(#g7)" role="img" aria-label="Photo of a cut cantaloupe melon"/></svg>
      <div class="group-text"><div class="group-name" style="color:var(--c-melons)">7 MELONS</div><p class="group-desc">It is a long established fact that a reader will be distracted by the readable content of a page when looking at its layout. The point of using Lorem</p></div>
    </div>
    <div class="cell">X</div><div class="cell">XX</div><div class="cell">X</div><div class="cell">XX</div><div class="cell">NR</div><div class="cell">X-NR</div><div class="cell">X</div><div class="cell">XX</div><div class="cell">XX</div>
  </div>

  <div class="chart-row">
    <div class="group">
      <svg class="group-photo" width="84" height="84" viewBox="0 0 84 84"><path d="M42 4A38 38 0 0 0 42 80" fill="none" stroke="var(--c-succulent)" stroke-width="5"/><defs><radialGradient id="g8"><stop offset="0" stop-color="#f0545a"/><stop offset="1" stop-color="#a3121e"/></radialGradient></defs><circle cx="45" cy="42" r="33" fill="url(#g8)" role="img" aria-label="Photo of red tomatoes"/></svg>
      <div class="group-text"><div class="group-name" style="color:var(--c-succulent)">8 SUCCULENT FOODS — TOMATOES</div><p class="group-desc">It is a long established fact that a reader will be distracted by the readable content of a page when looking at its layout. The point of using Lorem</p></div>
    </div>
    <div class="cell">NO</div><div class="cell">NO</div><div class="cell">X</div><div class="cell">XX</div><div class="cell">XX</div><div class="cell">XX</div><div class="cell">NO</div><div class="cell">NO</div><div class="cell">XX</div>
  </div>

  <div class="chart-row">
    <div class="group">
      <svg class="group-photo" width="84" height="84" viewBox="0 0 84 84"><path d="M42 4A38 38 0 0 0 42 80" fill="none" stroke="var(--c-veg)" stroke-width="5"/><defs><radialGradient id="g9"><stop offset="0" stop-color="#e2822a"/><stop offset="1" stop-color="#3f7a22"/></radialGradient></defs><circle cx="45" cy="42" r="33" fill="url(#g9)" role="img" aria-label="Photo of carrots, greens, cauliflower and peppers"/></svg>
      <div class="group-text"><div class="group-name" style="color:var(--c-veg)">9 VEGETABLES (Leafy. Flower. Root)</div><p class="group-desc">It is a long established fact that a reader will be distracted by the readable content of a page when looking at its layout. The point of using Lorem</p></div>
    </div>
    <div class="cell">NO</div><div class="cell">NO</div><div class="cell">X</div><div class="cell">XX</div><div class="cell">XX</div><div class="cell">XX</div><div class="cell">NO</div><div class="cell">XX</div><div class="cell">XX</div>
  </div>
</section>

<section class="principles">
  <h2>PRINCIPLES OF EATING</h2>
  <p>It is a long established fact that a reader will be distracted by the readable content of a page when looking at its layout. The point of using Lorem Ipsum is that it has a more-or-less normal distribution of letters, as opposed to using 'Content here, content here', making it look like readable English. Many desktop publishing packages and web page editors now use Lorem Ipsum as their default model text, and a search for 'lorem ipsum' will uncover many web sites still in their infancy. Various versions have evolved over the years, sometimes by accident, sometimes It is a long established fact that a reader will be distracted by the readable content of a page when looking at its layout. The point of using Lorem Ipsum is that it has a more-or-less normal distribution of letters, as opposed to using 'Content here, content here', making it look like readable English.</p>
</section>

</body>
</html>
```